Journeys With Marcella Business Cards

I need a business card design for my upscale Travel Agency.
Attached you can find my logo.
I would like to include the following:
- Name
- Title
- Phone Number
- Email
- Website
- and then something like: Follow us: JourneysWithMarcella (and then social media icons in color).
The logo should be in the front and then also the back.
I am also attaching a design that I liked (mostly for the layout) but open to any suggestions
Industry/Entity Type
Travel Agent
Contact Information for Business Card
Name: Marcella Dorn
Title: Travel Designer / Owner
Phone: 415-927-3308
Email: marcella@journeyswithmarcella-example.com
Website: www.JourneysWithMarcella-example.com
Social Media Handles for FB,IG, Twitter: JourneysWithMarcella
Colors
Designer to choose colors to be used in the design.
Look and feel

```html
<!DOCTYPE html>
<html lang="en">
<head>
<meta charset="UTF-8">
<title>Journeys With Marcella – Business Cards</title>
<link rel="stylesheet" href="https://fonts.googleapis.com/css2?family=Kaushan+Script&family=Lato:wght@400;700&display=swap">
<style>
  :root {
    --backdrop: #6b737d;
    --card-dark: #353230;
    --card-light: #ffffff;
    --accent: #f4a85a;
    --accent-deep: #e08a3c;
    --accent-soft: #f7c08a;
    --ink: #3a3a3a;
  }
  * { margin: 0; padding: 0; box-sizing: border-box; }
  html, body {
    width: 1200px;
    height: 900px;
    overflow: hidden;
  }
  body {
    background: var(--backdrop);
    font-family: "Lato", sans-serif;
    position: relative;
  }
  .card {
    position: absolute;
    left: 320px;
    width: 560px;
    height: 320px;
    box-shadow: 0 6px 18px rgba(0, 0, 0, 0.25);
  }
  .card--front {
    top: 100px;
    background: var(--card-dark);
    display: flex;
    align-items: center;
    justify-content: center;
  }
  .brand {
    display: flex;
    align-items: center;
    gap: 16px;
  }
  .brand__mark {
    width: 34px;
    height: 34px;
    background: var(--accent);
  }
  .brand__name {
    font-family: "Lato", sans-serif;
    font-weight: 700;
    font-size: 30px;
    color: var(--accent);
    letter-spacing: 0.5px;
  }
  .brand--small {
    gap: 8px;
    margin-bottom: 12px;
  }
  .brand--small .brand__mark {
    width: 14px;
    height: 14px;
  }
  .brand--small .brand__name {
    font-size: 14px;
    letter-spacing: 0.3px;
  }
  .card--back {
    top: 480px;
    background: var(--card-light);
    display: flex;
    flex-direction: column;
    align-items: center;
    justify-content: center;
    text-align: center;
  }
  .holder__name {
    font-family: "Kaushan Script", cursive;
    font-weight: 400;
    font-size: 42px;
    line-height: 1.1;
    color: var(--accent);
  }
  .holder__title {
    font-weight: 700;
    font-size: 16px;
    color: var(--accent);
    margin-top: 2px;
    letter-spacing: 0.5px;
  }
  .contact {
    margin-top: 10px;
    font-size: 14px;
    line-height: 1.45;
    color: var(--ink);
  }
  .follow {
    display: flex;
    align-items: center;
    gap: 10px;
    margin-top: 12px;
    font-size: 13px;
    color: var(--ink);
  }
  .follow__handle {
    font-weight: 700;
    color: var(--accent);
  }
  .social {
    display: flex;
    gap: 6px;
    list-style: none;
  }
  .social__dot {
    width: 22px;
    height: 22px;
    border-radius: 50%;
    background: var(--accent);
  }
  .social__dot--deep { background: var(--accent-deep); }
  .social__dot--soft { background: var(--accent-soft); }
  .social__dot--dark { background: var(--card-dark); }
</style>
</head>
<body>
  <section class="card card--front">
    <div class="brand">
      <span class="brand__mark"></span>
      <span class="brand__name">Journeys With Marcella</span>
    </div>
  </section>

  <section class="card card--back">
    <div class="brand brand--small">
      <span class="brand__mark"></span>
      <span class="brand__name">Journeys With Marcella</span>
    </div>
    <h1 class="holder__name">Marcella Dorn</h1>
    <p class="holder__title">Travel Designer / Owner</p>
    <p class="contact">
      415-927-3308 | marcella@journeyswithmarcella-example.com<br>
      www.JourneysWithMarcella-example.com
    </p>
    <div class="follow">
      <span>Follow us: <span class="follow__handle">JourneysWithMarcella</span></span>
      <ul class="social" aria-label="Social media profiles">
        <li class="social__dot"></li>
        <li class="social__dot social__dot--deep"></li>
        <li class="social__dot social__dot--dark"></li>
        <li class="social__dot social__dot--soft"></li>
      </ul>
    </div>
  </section>
</body>
</html>
```